Modern Minimal Velora Glow Set Retail Box

We need a design for our slide out packaging box. The packaging is for our Velora Glow Set, which includes a cleanser and a cream. We would love something that's original,minimal and modern and not gender specific. Feel free to use your own take on design. Surprise us. I've attached dimensions of the box as well as some refrence images of some boxes we like. It doesn't have to be exactly like these images but its a good starting point. Ive also attached our logo (you can change the logo style if needed to fit your design), your free to use other fonts and colors to match your design. The back of the box will have the drug fact for both products.

Target Market(s)

Everybody

Industry/Entity Type

Beauty

Font styles to use
Sans Serif

Colors
3176b5
33a6d7
85cae6
33b8a4
86cfc6
1b1b1b
ececec

Requirements
Must have
• Originality

```html
<!DOCTYPE html>
<html lang="en">
<head>
<meta charset="utf-8">
<title>Velora Glow Set – Box Dieline</title>
<link rel="stylesheet" href="https://fonts.googleapis.com/css2?family=Antonio:wght@100&family=Montserrat:wght@400;600&family=Crimson+Text&family=Lora&display=swap">
<style>
  :root {
    --blue-light: #85cae6;
    --teal: #33b8a4;
    --teal-light: #86cfc6;
    --blue-deep: #3176b5;
    --ink: #1b1b1b;
    --paper: #ffffff;
    --rule: #5c6a70;
  }
  html, body { margin: 0; width: 1200px; height: 1200px; overflow: hidden; background: var(--paper); }
  .artboard { display: block; width: 1200px; height: 1200px; }
  .panel-label { font-family: "Crimson Text", serif; font-size: 14px; fill: var(--ink); }
  .dim { font-family: "Crimson Text", serif; font-size: 8px; fill: var(--ink); }
  .fold { fill: none; stroke: var(--rule); stroke-width: 0.6; }
  .fold-faint { fill: none; stroke: var(--rule); stroke-width: 0.5; opacity: .35; }
  .guide { stroke: #9aa3a6; stroke-width: 0.5; }
  .title { font-family: "Antonio", sans-serif; font-weight: 100; fill: var(--paper); text-anchor: middle; }
  .subtitle { font-family: "Montserrat", sans-serif; font-weight: 400; fill: var(--paper); text-anchor: middle; letter-spacing: 1.5px; }
  .brand { font-family: "Montserrat", sans-serif; font-weight: 600; fill: var(--ink); text-anchor: middle; letter-spacing: .5px; }
  .badge { fill: var(--blue-deep); }
  .badge-text { font-family: "Lora", serif; font-size: 9.5px; fill: var(--paper); text-anchor: middle; letter-spacing: 1px; }
  .facts-box { fill: none; stroke: var(--ink); stroke-width: 1; }
  .facts-rule { stroke: var(--ink); stroke-width: .6; }
  .facts-head { font-family: "Montserrat", sans-serif; font-weight: 600; font-size: 5.5px; fill: var(--ink); }
  .facts-text { font-family: "Montserrat", sans-serif; font-size: 3px; fill: var(--ink); }
  .note-box { fill: none; stroke: var(--paper); stroke-width: .7; }
  .note-text { font-family: "Montserrat", sans-serif; font-size: 7.5px; fill: var(--paper); text-anchor: middle; }
  .note-text.strong { font-weight: 600; }
</style>
</head>
<body>
<svg class="artboard" viewBox="0 0 1200 1200" xmlns="http://www.w3.org/2000/svg">
  <defs>
    <linearGradient id="grad-sleeve-out" x1="0.45" y1="0.75" x2="0.85" y2="0.1">
      <stop offset="0" stop-color="#85cae6"/><stop offset="0.45" stop-color="#6fc3d6"/><stop offset="1" stop-color="#26b9a4"/>
    </linearGradient>
    <linearGradient id="grad-sleeve-in" x1="0.6" y1="0" x2="0.35" y2="1">
      <stop offset="0" stop-color="#85cae6"/><stop offset="0.35" stop-color="#80c9e2"/><stop offset="1" stop-color="#26b9a4"/>
    </linearGradient>
    <linearGradient id="grad-tray-out" x1="0" y1="0" x2="0" y2="1">
      <stop offset="0" stop-color="#85cae6"/><stop offset="0.3" stop-color="#7ec8e0"/><stop offset="0.75" stop-color="#26b9a4"/><stop offset="1" stop-color="#26b9a4"/>
    </linearGradient>
    <linearGradient id="grad-tray-in" x1="0.75" y1="0.1" x2="0.4" y2="0.75">
      <stop offset="0" stop-color="#26b9a4"/><stop offset="0.5" stop-color="#5fc0cc"/><stop offset="1" stop-color="#85cae6"/>
    </linearGradient>
  </defs>

  <!-- Sleeve outside -->
  <g class="sleeve-outside">
    <text class="panel-label" x="60" y="59">sleeve outside</text>
    <g class="guides">
      <line class="guide" x1="50" y1="44" x2="50" y2="80"/><line class="guide" x1="80" y1="44" x2="80" y2="80"/>
      <line class="guide" x1="231" y1="44" x2="231" y2="80"/><line class="guide" x1="316" y1="44" x2="316" y2="80"/>
      <line class="guide" x1="468" y1="44" x2="468" y2="80"/><line class="guide" x1="554" y1="44" x2="554" y2="80"/>
      <line class="guide" x1="50" y1="472" x2="50" y2="507"/><line class="guide" x1="80" y1="472" x2="80" y2="507"/>
      <line class="guide" x1="231" y1="472" x2="231" y2="507"/><line class="guide" x1="316" y1="472" x2="316" y2="507"/>
      <line class="guide" x1="468" y1="472" x2="468" y2="507"/><line class="guide" x1="554" y1="472" x2="554" y2="507"/>
      <line class="guide" x1="12" y1="82" x2="40" y2="82"/><line class="guide" x1="12" y1="111" x2="40" y2="111"/>
      <line class="guide" x1="12" y1="439" x2="40" y2="439"/><line class="guide" x1="12" y1="469" x2="40" y2="469"/>
      <line class="guide" x1="562" y1="82" x2="590" y2="82"/><line class="guide" x1="562" y1="111" x2="590" y2="111"/>
      <line class="guide" x1="562" y1="439" x2="590" y2="439"/><line class="guide" x1="562" y1="469" x2="590" y2="469"/>
    </g>
    <rect x="26" y="69" width="548" height="414" fill="url(#grad-sleeve-out)"/>
    <rect class="fold" x="50" y="82" width="504" height="387"/>
    <line class="fold" x1="50" y1="111" x2="554" y2="111"/><line class="fold" x1="50" y1="439" x2="554" y2="439"/>
    <line class="fold" x1="80" y1="82" x2="80" y2="469"/><line class="fold" x1="231" y1="82" x2="231" y2="469"/>
    <line class="fold" x1="316" y1="82" x2="316" y2="469"/><line class="fold" x1="468" y1="82" x2="468" y2="469"/>
    <text class="dim" x="154" y="73" text-anchor="middle">76mm</text>
    <text class="dim" x="272" y="73" text-anchor="middle">43mm</text>
    <text class="dim" x="388" y="73" text-anchor="middle">76mm</text>
    <text class="dim" x="506" y="73" text-anchor="middle">43mm</text>
    <text class="dim" x="564" y="257">165mm</text>

    <!-- front -->
    <text class="brand" x="155" y="175" font-size="22">Lirra Care</text>
    <text class="title" x="157" y="290" font-size="52" letter-spacing="2">VELORA</text>
    <text class="subtitle" x="155" y="304" font-size="9">GLOW SET</text>
    <circle class="badge" cx="155" cy="390" r="32"/>
    <text class="badge-text" x="155" y="384">cleanser</text>
    <text class="badge-text" x="155" y="393">+</text>
    <text class="badge-text" x="155" y="403">cream</text>

    <!-- spine -->
    <text class="brand" x="0" y="0" font-size="15" transform="translate(279 292) rotate(-90)">Lirra Care</text>

    <!-- back: facts -->
    <g class="drug-facts">
      <rect x="357" y="226" width="68" height="102" fill="var(--teal-light)" opacity=".25"/>
      <rect class="facts-box" x="357" y="226" width="68" height="102"/>
      <text class="facts-head" x="360" y="233">Drug Facts</text>
      <line class="facts-rule" x1="357" y1="235" x2="425" y2="235"/>
      <text class="facts-text" x="360" y="240">Active ingredient</text><text class="facts-text" x="406" y="240">Purpose</text>
      <text class="facts-text" x="360" y="244">Apply a thin layer daily</text>
      <line class="facts-rule" x1="357" y1="246" x2="425" y2="246"/>
      <text class="facts-text" x="360" y="251">Uses</text>
      <text class="facts-text" x="360" y="255">For external use only</text>
      <line class="facts-rule" x1="357" y1="260" x2="425" y2="260"/>
      <text class="facts-text" x="360" y="265">Warnings</text>
      <text class="facts-text" x="360" y="270">Avoid contact with eyes</text>
      <text class="facts-text" x="360" y="275">Stop use if irritation occurs</text>
      <line class="facts-rule" x1="357" y1="306" x2="425" y2="306"/>
      <text class="facts-text" x="360" y="311">Directions</text>
      <line class="facts-rule" x1="357" y1="317" x2="425" y2="317"/>
      <text class="facts-text" x="360" y="322">Inactive ingredients</text>
    </g>

    <!-- side spine -->
    <g transform="translate(511 292) rotate(-90)">
      <text class="title" x="0" y="6" font-size="40" letter-spacing="1.5">VELORA</text>
      <text class="subtitle" x="0" y="19" font-size="7">GLOW SET</text>
    </g>
  </g>

  <!-- Sleeve inside -->
  <g class="sleeve-inside">
    <text class="panel-label" x="649" y="59">sleeve inside</text>
    <rect x="630" y="98" width="547" height="361" fill="url(#grad-sleeve-in)"/>
    <rect class="fold" x="646" y="111" width="504" height="328"/>
    <line class="fold" x1="732" y1="111" x2="732" y2="439"/><line class="fold" x1="882" y1="111" x2="882" y2="439"/>
    <line class="fold" x1="968" y1="111" x2="968" y2="439"/><line class="fold" x1="1119" y1="111" x2="1119" y2="439"/>
  </g>

  <!-- Tray outside -->
  <g class="tray-outside">
    <text class="panel-label" x="85" y="584">tray outside</text>
    <g class="guides">
      <line class="guide" x1="195" y1="560" x2="195" y2="585"/><line class="guide" x1="271" y1="560" x2="271" y2="585"/>
      <line class="guide" x1="410" y1="560" x2="410" y2="585"/><line class="guide" x1="515" y1="560" x2="515" y2="585"/>
      <line class="guide" x1="166" y1="1138" x2="166" y2="1168"/><line class="guide" x1="195" y1="1138" x2="195" y2="1168"/>
      <line class="guide" x1="271" y1="1138" x2="271" y2="1168"/><line class="guide" x1="410" y1="1138" x2="410" y2="1168"/>
      <line class="guide" x1="515" y1="1138" x2="515" y2="1168"/>
      <line class="guide" x1="128" y1="628" x2="153" y2="628"/><line class="guide" x1="128" y1="704" x2="153" y2="704"/>
      <line class="guide" x1="128" y1="1025" x2="153" y2="1025"/><line class="guide" x1="128" y1="1101" x2="153" y2="1101"/>
      <line class="guide" x1="128" y1="1130" x2="153" y2="1130"/>
      <line class="guide" x1="529" y1="598" x2="554" y2="598"/><line class="guide" x1="529" y1="628" x2="554" y2="628"/>
      <line class="guide" x1="529" y1="704" x2="554" y2="704"/><line class="guide" x1="529" y1="1025" x2="554" y2="1025"/>
      <line class="guide" x1="529" y1="1101" x2="554" y2="1101"/><line class="guide" x1="529" y1="1130" x2="554" y2="1130"/>
    </g>
    <rect x="148" y="577" width="386" height="567" fill="url(#grad-tray-out)"/>
    <rect class="fold" x="271" y="598" width="139" height="30"/>
    <rect class="fold" x="271" y="628" width="139" height="76"/>
    <rect class="fold" x="166" y="704" width="349" height="321"/>
    <line class="fold" x1="195" y1="704" x2="195" y2="1025"/><line class="fold" x1="271" y1="704" x2="271" y2="1025"/>
    <line class="fold" x1="410" y1="704" x2="410" y2="1025"/><line class="fold" x1="486" y1="704" x2="486" y2="1025"/>
    <rect class="fold" x="271" y="1025" width="139" height="76"/>
    <rect class="fold" x="271" y="1101" width="139" height="29"/>
    <text class="dim" x="338" y="575" text-anchor="middle">70mm</text>
    <text class="dim" x="555" y="661">38mm</text>
    <text class="dim" x="555" y="869">162mm</text>
    <text class="dim" x="555" y="1066">38mm</text>

    <text class="brand" x="340" y="673" font-size="17">Lirra Care</text>

    <text class="title" x="340" y="852" font-size="48" letter-spacing="2">VELORA</text>
    <text class="subtitle" x="338" y="866" font-size="9">GLOW SET</text>
    <circle class="badge" cx="338" cy="922" r="32"/>
    <text class="badge-text" x="338" y="916">cleanser</text>
    <text class="badge-text" x="338" y="925">+</text>
    <text class="badge-text" x="338" y="935">cream</text>

    <g transform="translate(235 876) rotate(-90)">
      <text class="title" x="0" y="6" font-size="38" letter-spacing="1.5">VELORA</text>
      <text class="subtitle" x="0" y="18" font-size="7">GLOW SET</text>
    </g>
    <g transform="translate(452 880) rotate(90)">
      <text class="title" x="0" y="6" font-size="38" letter-spacing="1.5">VELORA</text>
      <text class="subtitle" x="0" y="18" font-size="7">GLOW SET</text>
    </g>

    <text class="brand" x="0" y="0" font-size="17" transform="translate(340 1058) rotate(180)">Lirra Care</text>
  </g>

  <!-- Tray inside -->
  <g class="tray-inside">
    <text class="panel-label" x="753" y="598">tray inside</text>
    <rect x="783" y="615" width="306" height="495" fill="url(#grad-tray-in)"/>
    <rect class="fold-faint" x="867" y="628" width="139" height="76"/>
    <rect class="fold" x="792" y="704" width="290" height="321"/>
    <line class="fold" x1="867" y1="704" x2="867" y2="1025"/><line class="fold" x1="1006" y1="704" x2="1006" y2="1025"/>
    <rect class="fold-faint" x="867" y="1025" width="139" height="76"/>
    <rect class="note-box" x="889" y="792" width="95" height="60"/>
    <text class="note-text strong" x="936" y="807">Lorem Ipsum is</text>
    <text class="note-text" x="936" y="822">simply dummy text</text>
    <text class="note-text" x="936" y="837">of the printing and</text>
  </g>
</svg>
</body>
</html>
```